Bref créative
Stationery for interior design business
Venmark Interiors, LLC
Simple
Cleo Venmark
Interior Designer
No address on card or stationery
cleo@venmarkinteriors.example
venmarkinteriors.example
Please also include my blog address on the front of the card: cleovenmark.example
Open for design suggestions, but I'd like either the entire logo or only the sphere to appear on the back

```html
<!DOCTYPE html>
<html lang="en">
<head>
<meta charset="utf-8">
<title>Venmark Interiors — Business Card</title>
<link href="https://fonts.googleapis.com/css2?family=Lato:wght@400;700&display=swap" rel="stylesheet">
<style>
  :root{
    --backdrop:#ecebe8;
    --card-white:#ffffff;
    --brand-blue:#3447b0;
    --brand-blue-deep:#2a3a97;
    --swoosh-gray:#6d6e72;
    --ink-dark:#3a3b3f;
    --text-light:#ffffff;
    --divider:rgba(255,255,255,.75);
  }
  *{box-sizing:border-box;margin:0;padding:0}
  html,body{width:1200px;height:914px;overflow:hidden;background:var(--backdrop)}
  body{font-family:'Lato',sans-serif;position:relative}
  .business-card{
    position:absolute;left:100px;top:171px;width:1000px;height:571px;
    background:var(--card-white);overflow:hidden;
    box-shadow:0 10px 30px rgba(0,0,0,.18);
  }
  .card-waves{position:absolute;inset:0}
  .brand-mark{
    position:absolute;left:455px;top:120px;display:flex;align-items:center;gap:16px;
  }
  .brand-dot{width:58px;height:58px;border-radius:50%;background:var(--brand-blue)}
  .brand-name{
    font-size:40px;font-weight:700;color:var(--ink-dark);letter-spacing:.5px;line-height:1;
  }
  .contact-area{
    position:absolute;left:0;right:0;top:370px;display:flex;justify-content:center;
    color:var(--text-light);
  }
  .identity{
    text-align:right;padding-right:22px;border-right:2px solid var(--divider);
    display:flex;flex-direction:column;gap:7px;
  }
  .identity .person-name{font-size:25px;font-weight:700}
  .identity .person-role{font-size:21px}
  .identity .blog{font-size:21px;margin-top:6px}
  .contact-list{list-style:none;padding-left:22px;display:flex;flex-direction:column;gap:11px}
  .contact-list li{display:flex;align-items:center;gap:12px;font-size:21px}
  .contact-icon{width:24px;height:24px;flex:none}
</style>
</head>
<body>
  <div class="business-card">
    <svg class="card-waves" width="1000" height="571" viewBox="0 0 1000 571" aria-hidden="true">
      <defs>
        <linearGradient id="blueFill" x1="0" y1="0" x2="0" y2="1">
          <stop offset="0" stop-color="var(--brand-blue)"/>
          <stop offset="1" stop-color="var(--brand-blue-deep)"/>
        </linearGradient>
      </defs>
      <path d="M0 240 C 300 330, 620 180, 1000 170 L1000 571 L0 571 Z" fill="var(--swoosh-gray)"/>
      <path d="M0 272 C 320 350, 630 225, 1000 215 L1000 571 L0 571 Z" fill="url(#blueFill)"/>
    </svg>

    <div class="brand-mark">
      <span class="brand-dot"></span>
      <span class="brand-name">Venmark Interiors</span>
    </div>

    <div class="contact-area">
      <div class="identity">
        <span class="person-name">Cleo Venmark</span>
        <span class="person-role">Interior Designer</span>
        <span class="blog">www.cleovenmark.example</span>
      </div>
      <ul class="contact-list">
        <li>
          <svg class="contact-icon" viewBox="0 0 24 24" aria-hidden="true"><circle cx="12" cy="12" r="12" fill="#fff"/><path d="M8.5 6.5l2 2-1.2 1.6a8 8 0 0 0 4.6 4.6l1.6-1.2 2 2-1.4 1.9C11.6 17 7 12.4 6.6 7.9z" fill="var(--brand-blue)"/></svg>
          555-014-2290
        </li>
        <li>
          <svg class="contact-icon" viewBox="0 0 24 24" aria-hidden="true"><circle cx="12" cy="12" r="12" fill="#fff"/><rect x="6" y="8" width="12" height="8.5" rx="1" fill="var(--brand-blue)"/><path d="M6.5 8.6l5.5 4.3 5.5-4.3" stroke="#fff" stroke-width="1.2" fill="none"/></svg>
          cleo@venmarkinteriors.example
        </li>
        <li>
          <svg class="contact-icon" viewBox="0 0 24 24" aria-hidden="true"><circle cx="12" cy="12" r="12" fill="#fff"/><g fill="none" stroke="var(--brand-blue)" stroke-width="1.3"><circle cx="12" cy="12" r="6"/><ellipse cx="12" cy="12" rx="2.6" ry="6"/><path d="M6 12h12"/></g></svg>
          www.venmarkinteriors.example
        </li>
      </ul>
    </div>
  </div>
</body>
</html>
```